Business card for a Exhibition booth fabrication company

Hi. My company would like to change our corporate name card. We are an events and Exhibition stand builder company. We would like our corporate name card to resonate what we do. I need someone to create something unique that relates to the industry that I am in. The graphic designer should be creative to incorporate the elements of my industry and try to blend in well in the design of the card. Our aim is to ensure that we are unique and our card can look different from our competitors.
Updates

The decision maker was very busy and didnt had time to make this decision

Target Market(s)

Marketing and events manager from all companies

Contact Information for Business Card

The business card should have the following details:
Name
Job Title
Email
Website

Colors

Designer to choose colors to be used in the design.

Requirements
Must have
• The card must be look something that is relevant to the service that I am providing. My website is: www.velmora-builds.com
• You can see my website to get more information on what service that I am doing
Nice to have
• On the back of my card, I would like to have a globe image with the incorporation of my company logo. This is to indicate that my services can be done in any part of the world.

```html
<!DOCTYPE html>
<html lang="en">
<head>
<meta charset="utf-8">
<title>Velmora Builds – Business Card</title>
<link href="https://fonts.googleapis.com/css2?family=Montserrat:wght@400;600;700&family=Open+Sans:wght@400;600&display=swap" rel="stylesheet">
<style>
  :root {
    --page-bg: #e6e4e1;
    --card-dark: #2e2e30;
    --card-dark-edge: #252527;
    --card-light: #ffffff;
    --card-light-shade: #f1f1f1;
    --accent-red: #e31e24;
    --ink-dark: #4a4a4c;
    --ink-mid: #5c5c5e;
    --brand-grey: #8a8a8c;
    --globe-tone: #3a3a3d;
    --tagline: #e8e8e8;
  }
  * { margin: 0; padding: 0; box-sizing: border-box; }
  html, body {
    width: 1200px; height: 900px; overflow: hidden;
    background: var(--page-bg);
  }
  .canvas {
    position: relative; width: 1200px; height: 900px;
  }
  .card {
    position: absolute; left: 250px; width: 700px; height: 400px;
    box-shadow: 0 6px 18px rgba(0,0,0,.18);
    overflow: hidden;
  }
  /* Back side */
  .card-back {
    top: 40px;
    background: linear-gradient(160deg, var(--card-dark) 0%, var(--card-dark-edge) 100%);
  }
  .globe-art {
    position: absolute; left: 150px; top: 20px; width: 460px; height: 360px;
    border-radius: 50%;
    background: radial-gradient(circle at 55% 40%, var(--globe-tone) 0%, rgba(58,58,61,.5) 55%, rgba(46,46,48,0) 72%);
  }
  .brand-lockup {
    position: absolute; left: 0; right: 0; top: 150px;
    display: flex; align-items: center; justify-content: center; gap: 18px;
  }
  .brand-dot {
    width: 26px; height: 26px; border-radius: 50%;
    background: var(--accent-red);
  }
  .brand-name {
    font-family: "Montserrat", sans-serif; font-weight: 400;
    font-size: 38px; letter-spacing: 8px; color: var(--brand-grey);
  }
  .tagline {
    position: absolute; left: 0; right: 0; top: 222px; text-align: center;
    font-family: "Open Sans", sans-serif; font-size: 17px;
    letter-spacing: .5px; color: var(--tagline);
  }
  /* Front side */
  .card-front {
    top: 470px;
    background: linear-gradient(135deg, var(--card-light) 40%, var(--card-light-shade) 100%);
  }
  .identity {
    position: absolute; right: 388px; top: 152px; text-align: right;
  }
  .person-name {
    font-family: "Montserrat", sans-serif; font-weight: 700;
    font-size: 28px; letter-spacing: -.5px; color: var(--ink-dark);
  }
  .job-title {
    margin-top: 2px;
    font-family: "Montserrat", sans-serif; font-weight: 400;
    font-size: 20px; color: var(--accent-red);
  }
  .contact-block {
    position: absolute; left: 324px; top: 150px;
    display: flex; align-items: stretch;
  }
  .contact-icons {
    display: flex; flex-direction: column; justify-content: space-between;
    padding: 6px 0; width: 22px; height: 88px;
  }
  .contact-icons svg { width: 16px; height: 16px; display: block; }
  .divider {
    width: 2px; background: var(--accent-red); margin: 0 12px 0 8px;
  }
  .contact-lines {
    list-style: none;
    font-family: "Open Sans", sans-serif; font-size: 19px;
    color: var(--ink-mid); line-height: 29px;
  }
</style>
</head>
<body>
<main class="canvas">
  <section class="card card-back">
    <div class="globe-art" role="img" aria-label="Faint world globe map in dark grey tones"></div>
    <div class="brand-lockup">
      <span class="brand-dot"></span>
      <span class="brand-name">VELMORA BUILDS</span>
    </div>
    <p class="tagline">Turning Conceptions Into Reality</p>
  </section>

  <section class="card card-front">
    <div class="identity">
      <h1 class="person-name">YOUR NAME</h1>
      <p class="job-title">JOB TITLE</p>
    </div>
    <div class="contact-block">
      <div class="contact-icons">
        <svg viewBox="0 0 16 16" aria-hidden="true"><rect x="4" y="1" width="8" height="14" rx="1.5" fill="none" stroke="#e31e24" stroke-width="1.5"/><line x1="7" y1="12.5" x2="9" y2="12.5" stroke="#e31e24" stroke-width="1.2"/></svg>
        <svg viewBox="0 0 16 16" aria-hidden="true"><rect x="1" y="3" width="14" height="10" fill="#e31e24"/><polyline points="1,3 8,9 15,3" fill="none" stroke="#fff" stroke-width="1.2"/></svg>
        <svg viewBox="0 0 16 16" aria-hidden="true"><circle cx="8" cy="8" r="6.5" fill="none" stroke="#e31e24" stroke-width="1.3"/><ellipse cx="8" cy="8" rx="3" ry="6.5" fill="none" stroke="#e31e24" stroke-width="1"/><line x1="1.5" y1="8" x2="14.5" y2="8" stroke="#e31e24" stroke-width="1"/></svg>
      </div>
      <span class="divider"></span>
      <ul class="contact-lines">
        <li>000 000 0000</li>
        <li>youremail@xyz.com</li>
        <li>www.velmora-builds.com</li>
      </ul>
    </div>
  </section>
</main>
</body>
</html>
```